Logo and packaging design for a food brand: Amber Hollow

Dear designer,

I'm located in Vancouver, British Columbia, Canada, and I'm launching a brand of products made of beef tallow. It's called Amber Hollow. I'm ultimately looking for a designer that can help me build the brand and create a series of products.

Here is what I need at this point:

- A logo for Amber Hollow (playing with the letters A and H - sketch using ChatGPT attached)
- A packaging design for the PREMIUM WAGYU TALLOW - 235 ml (= 8 oz: https://www.jarvelo-supply.example/Product/Detail/K-40261M-TN/Jars/Clear-Straight-Sided-Glass-Jars-8-oz-Black-Plastic-Cap)
- Glass jar with a label all around it and a lid seal label
- Primary colours: black, white, gold
- Secondary colours if needed: Canada red and light grey
- Fonts: not specified, looking forward to your inputs on what works
- Please refer to our #1 competitor as reference: https://www.northbrimlarder.example/collections/products (we like their design style as well)
- #2 competitor to be used as reference: https://quellmoor.example/products/1-jar-14-0-oz-organic-grass-fed-beef-tallow

- Information for the packaging:
PREMIUM WAGYU BEEF TALLOW
100% PURE
(optional) PRODUCED IN CANADA
NUTRITIONAL VALUE (we don't have the numbers yet, but please create a placeholder/mockup for this section)
* You can also add more information following the example from our Competitor 01

- Please feel free to improve the logo, but keep the concept of Amber Hollow (or AH) + the face of a bull
- Finally, I'd also love to see two colour schemes: one dark and one bright - I hope it's not asking too much

Target Market(s)

North America

Industry/Entity Type

Food

Font styles to use
Sans Serif
Script

Colors
FFC000
F8CF3A
FAE287
FDF2CF
FEFAEE

Requirements
Must have
• Incorporate gold, black and white
Nice to have
• Play with the letters AH in the logo (company name: Amber Hollow)
Should not have
• Many colours

```html
<!DOCTYPE html>
<html lang="en">
<head>
<meta charset="UTF-8">
<title>Amber Hollow – Wagyu Beef Tallow Packaging</title>
<link rel="stylesheet" href="https://fonts.googleapis.com/css2?family=Oswald:wght@600;700&family=Montserrat:wght@600;700&display=swap">
<style>
  :root {
    --canvas: #f6f2ec;
    --label-black: #232222;
    --ink-white: #ffffff;
    --gold-light: #f4e3a1;
    --gold: #d7b45a;
    --gold-deep: #9c7a2c;
    --canada-red: #6e1414;
    --lid-black: #1d1b1a;
    --lid-rim: #2c2927;
  }
  * { margin: 0; padding: 0; box-sizing: border-box; }
  html, body { width: 1200px; height: 800px; overflow: hidden; }
  body {
    background: var(--canvas);
    font-family: "Montserrat", sans-serif;
    position: relative;
  }

  /* ---------- Wrap-around label ---------- */
  .jar-label {
    position: absolute;
    left: 50px;
    top: 165px;
    width: 690px;
    height: 470px;
    background: var(--label-black);
    box-shadow: 0 6px 18px rgba(0,0,0,.18);
    overflow: hidden;
  }
  .premium-tag {
    position: absolute;
    left: 0;
    top: 52px;
    width: 160px;
    height: 36px;
    background: var(--canada-red);
    border: 2px solid var(--gold);
    border-left: none;
    border-radius: 0 18px 18px 0;
    color: var(--ink-white);
    font-weight: 700;
    font-size: 17px;
    letter-spacing: 2px;
    display: flex;
    align-items: center;
    justify-content: center;
  }
  .brand-header {
    position: absolute;
    left: 200px;
    top: 34px;
    display: flex;
    align-items: center;
    gap: 22px;
    color: var(--ink-white);
    font-weight: 600;
    font-size: 28px;
    letter-spacing: 6px;
  }
  .brand-mark {
    width: 62px;
    height: 62px;
    border-radius: 50%;
    background: linear-gradient(145deg, var(--gold-light), var(--gold-deep));
  }
  .product-title {
    position: absolute;
    left: 50px;
    top: 118px;
    font-family: "Oswald", sans-serif;
    font-weight: 700;
    font-size: 78px;
    line-height: 1.06;
    color: var(--ink-white);
    letter-spacing: 1px;
  }
  .bull-illustration {
    position: absolute;
    left: 312px;
    top: 124px;
    width: 330px;
    height: 326px;
    border-radius: 46% 40% 28% 34%;
    background: radial-gradient(ellipse at 42% 38%, var(--gold-light), var(--gold) 50%, rgba(156,122,44,0.35) 78%, transparent 100%);
  }
  .purity-seal {
    position: absolute;
    right: 46px;
    top: 130px;
    width: 92px;
    height: 92px;
    border-radius: 50%;
    background: radial-gradient(circle, var(--gold-light), var(--gold) 70%, var(--gold-deep));
    display: flex;
    align-items: center;
    justify-content: center;
  }
  .purity-seal .seal-core {
    width: 70px;
    height: 70px;
    border-radius: 50%;
    border: 2px solid var(--gold-deep);
    display: flex;
    flex-direction: column;
    align-items: center;
    justify-content: center;
    color: var(--canada-red);
  }
  .seal-core .seal-value { font-family: "Oswald", sans-serif; font-weight: 700; font-size: 19px; line-height: 1; }
  .seal-core .seal-word { font-weight: 700; font-size: 10px; letter-spacing: 2px; margin-top: 3px; }
  .net-weight {
    position: absolute;
    left: 24px;
    bottom: 30px;
    color: var(--ink-white);
    font-family: "Oswald", sans-serif;
    font-weight: 600;
    font-size: 12px;
    letter-spacing: .5px;
  }
  .gold-band {
    position: absolute;
    left: 0;
    right: 0;
    bottom: 0;
    height: 12px;
    background: linear-gradient(90deg, var(--gold-deep), var(--gold-light) 45%, var(--gold) 70%, var(--gold-deep));
  }

  /* ---------- Lid seal label ---------- */
  .lid-seal {
    position: absolute;
    left: 790px;
    top: 225px;
    width: 360px;
    height: 360px;
  }
</style>
</head>
<body>

  <section class="jar-label" aria-label="Wrap-around jar label">
    <div class="premium-tag">PREMIUM</div>
    <div class="brand-header">
      <span class="brand-name">AMBER</span>
      <span class="brand-mark" aria-hidden="true"></span>
      <span class="brand-name">HOLLOW</span>
    </div>
    <h1 class="product-title">WAGYU<br>BEEF<br>TALLOW</h1>
    <div class="bull-illustration" role="img" aria-label="Gold engraved illustration of a standing bull"></div>
    <div class="purity-seal">
      <div class="seal-core">
        <span class="seal-value">100%</span>
        <span class="seal-word">PURE</span>
      </div>
    </div>
    <p class="net-weight">NET WT. 8 OZ (236ML)</p>
    <div class="gold-band"></div>
  </section>

  <svg class="lid-seal" viewBox="0 0 360 360" aria-label="Lid seal label">
    <defs>
      <linearGradient id="goldText" x1="0" y1="0" x2="1" y2="1">
        <stop offset="0" stop-color="#f4e3a1"/>
        <stop offset="1" stop-color="#b38f3c"/>
      </linearGradient>
      <path id="sealRing" d="M180,180 m-112,0 a112,112 0 1,1 224,0 a112,112 0 1,1 -224,0"/>
    </defs>
    <circle cx="180" cy="180" r="172" fill="#2c2927"/>
    <circle cx="180" cy="180" r="160" fill="#1d1b1a"/>
    <circle cx="180" cy="180" r="140" fill="#232222" stroke="#3a3633" stroke-width="2"/>
    <rect class="tamper-strip" x="150" y="-4" width="60" height="368" fill="#2a2828"/>
    <circle cx="180" cy="180" r="138" fill="#232222"/>
    <text font-family="Montserrat, sans-serif" font-weight="600" font-size="20" letter-spacing="5" fill="url(#goldText)">
      <textPath href="#sealRing">AMBER HOLLOW • AMBER HOLLOW •</textPath>
    </text>
    <circle cx="180" cy="180" r="48" fill="url(#goldText)"/>
    <text x="180" y="350" text-anchor="middle" font-family="Montserrat, sans-serif" font-weight="600" font-size="9" letter-spacing="2" fill="#d7b45a">AMBER HOLLOW</text>
  </svg>

</body>
</html>
```